Create a newspaper layout from word files and photos provided for wedding

For our wedding we want a "newspaper style" memento for guests. It will include articles I have written about me and my fiancee and our family and friends as well as photos and anecdotes.
We require someone to take our words and design content and turn it into a file that we can get printed.
We will provde content - we want your layout skill.

Full file is available at
https://www.filecrate.example/sh/q7wkbr2m41xpt9/ZZQmTLrhWvkpFGsYcNbVdEoUx?oref=e&n=715204368

Instructions are included.Utilise written content to create wedding newspaper and add photos were possible.
Black and white but photos should be in colour.
Must be 4 or 8 pages.
If text provided is too long notes to be provided to us where cuts are required.

We have committed payment.
We seek designs to review on Sunday evening.
We will select designs at this time or earlier if appropriate design is submitted using full layout.
Once selected we will work with designer to refine and finalise job by Tuesday next week when it must go to printer.

Thanks and if there are an questions post away.

Reason: Extended deadline due to file changes. We require the file to be available to select from by Sunday 12 April 8pm - ignore the Thursday deadline.

Target Market(s)

Wedding guests

Industry/Entity Type

Wedding

Font styles to use
Serif

Requirements
Must have
• Style and photographs
Should not have
• Too much blank space
• Too small text

```html
<!DOCTYPE html>
<html lang="en">
<head>
<meta charset="utf-8">
<title>Arts and Entertainment – page 3</title>
<link rel="stylesheet" href="https://fonts.googleapis.com/css2?family=Libre+Baskerville:ital,wght@0,400;0,700;1,400&family=Crimson+Text:ital,wght@0,400;0,600;1,400&family=Arimo:wght@400;700&display=swap">
<style>
:root{
  --ink:#111;
  --paper:#fff;
  --rule:#8a8a8a;
  --rule-light:#bdbdbd;
  --frame:#777;
  --muted:#777;
  --photo-stage:#5b3b26;
  --photo-stage-2:#2b1d15;
  --photo-room:#8a6e58;
  --photo-room-2:#c9b7a1;
  --photo-dojo:#b7aa9c;
  --photo-dojo-2:#3b1616;
}
*{box-sizing:border-box;margin:0;padding:0}
html,body{width:776px;height:1200px;overflow:hidden;background:var(--paper)}
body{position:relative;font-family:"Crimson Text",Georgia,serif;color:var(--ink)}
.page{position:relative;width:776px;height:1200px}

.folio-rule-top{position:absolute;left:14px;top:26px;width:748px;height:2px;background:var(--rule-light)}
.folio{position:absolute;left:14px;top:33px;width:748px;height:20px;font-family:"Libre Baskerville",Georgia,serif;font-weight:700;font-variant:small-caps;font-size:15px;line-height:20px}
.folio-date{position:absolute;left:0;top:0;letter-spacing:.2px}
.folio-section{position:absolute;right:34px;top:-2px;font-size:19px;letter-spacing:.5px}
.folio-number{position:absolute;right:0;top:-8px;padding-left:8px;border-left:2px solid var(--rule);font-size:17px;font-weight:400;height:22px}
.folio-rule-bottom{position:absolute;left:14px;top:55px;width:748px;height:4px;background:var(--rule)}

.headline{position:absolute;left:0;top:78px;width:776px;text-align:center;font-family:"Libre Baskerville",Georgia,serif;font-weight:700;font-size:45px;letter-spacing:.3px}

.photo{position:absolute}
.photo-stage{left:14px;top:157px;width:243px;height:351px;background:linear-gradient(160deg,var(--photo-stage),var(--photo-stage-2))}
.photo-family{left:266px;top:157px;width:244px;height:183px;background:linear-gradient(150deg,var(--photo-room),var(--photo-room-2))}
.photo-guitar{left:266px;top:349px;width:244px;height:159px;background:linear-gradient(160deg,var(--photo-stage),var(--photo-stage-2))}
.photo-iaido{left:519px;top:685px;width:242px;height:330px;background:linear-gradient(90deg,var(--photo-dojo) 0%,var(--photo-dojo) 55%,var(--photo-dojo-2) 100%)}

.story{position:absolute;left:519px;top:157px;width:244px;font-size:10.6px;line-height:12.6px;text-align:justify}
.story p{margin-bottom:0}
.story .lede::first-letter{float:left;font-family:"Libre Baskerville",Georgia,serif;font-weight:700;font-size:37px;line-height:30px;margin:2px 5px 0 0}
.story .pull{font-style:italic;font-size:14px;line-height:17px;margin:10px 0 10px;text-align:left}
.story .after{margin-top:0}

.divider{position:absolute;left:14px;top:532px;width:748px;height:4px;background:var(--rule)}

.crossword{position:absolute;left:15px;top:553px;width:490px;height:624px;border:4px solid var(--frame);font-family:"Arimo",Arial,sans-serif}
.cw-name{position:absolute;left:263px;top:23px;font-size:12px}
.cw-name span{display:inline-block;width:163px;border-bottom:1px solid var(--ink);margin-left:2px}
.cw-title{position:absolute;left:0;top:41px;width:490px;padding-left:30px;text-align:center;font-weight:700;font-size:14.5px}
.cw-sub{position:absolute;left:0;top:61px;width:490px;padding-left:30px;text-align:center;font-size:8.5px}
.cw-credit{position:absolute;right:30px;top:447px;font-size:7px;color:var(--muted)}
.cw-credit u{color:var(--muted)}
.clues{position:absolute;top:457px;font-size:8px;line-height:9.6px}
.clues h3{font-size:9px;text-decoration:underline;font-weight:700;margin-bottom:1px}
.clues ol{list-style:none}
.clues li{padding-left:10px;text-indent:-10px}
.clues b{font-weight:700}
.clues-across{left:31px;width:200px}
.clues-down{left:231px;width:205px}
.grid{position:absolute;left:0;top:0;overflow:visible}
.grid text{font-family:"Arimo",Arial,sans-serif;font-size:6px;fill:var(--ink)}

.sidebar-title{position:absolute;left:519px;width:242px;text-align:center;font-family:"Libre Baskerville",Georgia,serif;font-weight:700;font-size:24px}
.sidebar-sub{position:absolute;left:519px;width:242px;text-align:center;font-family:"Crimson Text",Georgia,serif;font-size:18px}
.sidebar-text{position:absolute;left:519px;width:242px;text-align:center;font-size:11.4px;line-height:13.6px}
.fact-rule{position:absolute;left:519px;top:1036px;width:242px;height:4px;background:var(--rule-light)}
</style>
</head>
<body>
<main class="page">
  <div class="folio-rule-top"></div>
  <header class="folio">
    <span class="folio-date">Saturday, 18 April, 2015 · The Chapel Daily</span>
    <span class="folio-section">Arts and Entertainment</span>
    <span class="folio-number">3</span>
  </header>
  <div class="folio-rule-bottom"></div>

  <h1 class="headline">The Russians are coming!!!</h1>

  <div class="photo photo-stage" role="img" aria-label="Photo: Anton performing on stage, singing into a microphone with a guitar"></div>
  <div class="photo photo-family" role="img" aria-label="Photo: Anton, Irina and their son singing together at home"></div>
  <div class="photo photo-guitar" role="img" aria-label="Photo: Anton singing and playing guitar on stage"></div>

  <article class="story">
    <p class="lede">The performance artists of Melbourne are in preparation today for the pending arrival of Russian couple Anton and Irina Veselov, veterans of the Moscow stage and performance industry. In town for the wedding of Anton's sister Clara, the Melbournians are hoping to be able to see a little of the eclectic but sublime grace of this couple.</p>
    <p>Irina Veselov is known for the spectrum of experience she brings to the art of stagecraft. Working alongside Russian stage royalty as well as teaching young children the fun associated with stage brings that lovely blend of exuberance and grace.</p>
    <p class="pull">Anton Veselov has hung up the guitar (see inset) but continues to be a regular performer across Moscow in a range of seasonal and ongoing productions in addition to his mentoring of young and upcoming actors.</p>
    <p class="after">A man of many talents Anton is also proficient (he is a qualified instructor) in the ancient Japanese art of Iaido, a sword technique that when perfected can render the sword back in the scabbard before the victim realizes they are dead. With them will be their five year old son Mikhail Veselov, with the artistic blood in his veins this young man is already wowing them in poetry recital competitions across Greater Moscow.</p>
  </article>

  <div class="divider"></div>

  <section class="crossword">
    <div class="cw-name">Name:<span></span></div>
    <h2 class="cw-title">Stations of the Crossword</h2>
    <p class="cw-sub">Be the first to give a complete copy to the MC and win a prize</p>
    <p class="cw-credit">Created on <u>PuzzleDesk.example Crossword Maker</u></p>

    <div class="clues clues-across">
      <h3>Across</h3>
      <ol>
        <li><b>1.</b> Flowergirls, Sofia and ???</li>
        <li><b>6.</b> Avenue where Clara and Hamish first lived together (6-3)</li>
        <li><b>9.</b> Clara and Hamish's first every holiday destination</li>
        <li><b>11.</b> Where Clara and Hamish are going on their honeymoon</li>
        <li><b>12.</b> Fast paced hobby that Hamish introduced Clara to</li>
        <li><b>13.</b> Clara's first suburb in Melbourne</li>
        <li><b>17.</b> Clara and Hamish had their first date at this Prahran restaurant (3-6)</li>
        <li><b>18.</b> Hamish's home towm</li>
        <li><b>19.</b> Sofia's middle name</li>
      </ol>
    </div>
    <div class="clues clues-down">
      <h3>Down</h3>
      <ol>
        <li><b>2.</b> Clara's home town</li>
        <li><b>3.</b> Where Hamish proposed to Clara</li>
        <li><b>4.</b> Which company produces Bella Notte lingerie (3-2-5)</li>
        <li><b>5.</b> Hamish's football number</li>
        <li><b>7.</b> Where Hamish had his first 'professional' job</li>
        <li><b>8.</b> Number of fish caught during their relationship (excluding Bucks day)</li>
        <li><b>10.</b> Anton's first primary school</li>
        <li><b>14.</b> Where Clara and Hamish met</li>
        <li><b>15.</b> Which Veselov has flown a glider?</li>
        <li><b>16.</b> Name of Sofia's childcare (3-5)</li>
      </ol>
    </div>
  </section>

  <svg class="grid" width="776" height="1200" viewBox="0 0 776 1200" aria-label="Crossword grid">
    <defs>
      <pattern id="cell" patternUnits="userSpaceOnUse" x="84" y="630" width="16.75" height="16.75">
        <rect x="0" y="0" width="16.75" height="16.75" fill="#fff" stroke="#333" stroke-width="1"/>
      </pattern>
    </defs>
    <g fill="url(#cell)" stroke="#333" stroke-width="1">
      <!-- down words -->
      <rect x="218" y="630" width="16.75" height="134"/>
      <rect x="134.25" y="680.25" width="16.75" height="100.5"/>
      <rect x="268.25" y="680.25" width="16.75" height="167.5"/>
      <rect x="84" y="697" width="16.75" height="83.75"/>
      <rect x="335.25" y="713.75" width="16.75" height="134"/>
      <rect x="402.25" y="730.5" width="16.75" height="67"/>
      <rect x="201.25" y="747.25" width="16.75" height="150.75"/>
      <rect x="167.75" y="847.75" width="16.75" height="67"/>
      <rect x="301.75" y="847.75" width="16.75" height="67"/>
      <rect x="234.75" y="864.5" width="16.75" height="117.25"/>
      <!-- across words -->
      <rect x="201.25" y="630" width="83.75" height="16.75"/>
      <rect x="167.75" y="697" width="150.75" height="16.75"/>
      <rect x="84" y="747.25" width="167.5" height="16.75"/>
      <rect x="301.75" y="747.25" width="134" height="16.75"/>
      <rect x="201.25" y="780.75" width="184.25" height="16.75"/>
      <rect x="301.75" y="814.25" width="100.5" height="16.75"/>
      <rect x="167.75" y="881.25" width="150.75" height="16.75"/>
      <rect x="201.25" y="948.25" width="100.5" height="16.75"/>
      <rect x="167.75" y="981.75" width="83.75" height="16.75"/>
    </g>
    <g>
      <text x="202.5" y="636.5">1</text>
      <text x="219.5" y="636.5">2</text>
      <text x="135.5" y="686.5">3</text>
      <text x="269.5" y="686.5">4</text>
      <text x="85.5" y="703.5">5</text>
      <text x="169" y="703.5">6</text>
      <text x="336.5" y="720">7</text>
      <text x="403.5" y="737">8</text>
      <text x="85.5" y="753.5">9</text>
      <text x="202.5" y="753.5">10</text>
      <text x="303" y="753.5">11</text>
      <text x="202.5" y="787">12</text>
      <text x="303" y="820.5">13</text>
      <text x="169" y="854">14</text>
      <text x="303" y="854">15</text>
      <text x="236" y="871">16</text>
      <text x="169" y="887.5">17</text>
      <text x="202.5" y="954.5">18</text>
      <text x="169" y="988">19</text>
    </g>
  </svg>

  <aside>
    <h2 class="sidebar-title" style="top:552px">Fun fact</h2>
    <p class="sidebar-sub" style="top:580px">iaido</p>
    <p class="sidebar-text" style="top:605px">A Japanese martial art associated with the smooth, controlled movements of drawing the sword from its scabbard, striking or cutting an opponent, removing blood from the blade, and then replacing the sword in the scabbard.</p>
    <div class="photo photo-iaido" role="img" aria-label="Photo: Anton in a white training uniform, drawing a sword from its scabbard"></div>
    <div class="fact-rule"></div>
    <h2 class="sidebar-title" style="top:1048px">Interesting fact</h2>
    <p class="sidebar-sub" style="top:1076px">Gorka</p>
    <p class="sidebar-text" style="top:1106px">At Russian weddings the first toast is made to the newlyweds and after the first shot, the guests begin to shout Gorko, Gorko, Gorko,…. Gorko means “bitter”. At this point the couple must kiss for a long time to take out the bitter taste of the vodka.</p>
  </aside>
</main>
</body>
</html>
```